Calm Fern Healthcare- Aged Care and Community Services

Looking for brochure to advertise our services. I will attach a draft that we do not want to use. Looking for graphics that are as natural as possible to present a personalised service. We supply services to aged people and people with disability. Please make it look classy and professional at the same time. I am looking for creativity. I have also attached the logo. Site addresses can be the last page. ideally looking for 2 designs, one A4 and another smaller possibly DL. Looking for creative out of the box thinkers. Thank you.

Target Market(s)

Aged Care service providers, disability service providers and private hospitals

Font styles to use
Serif
Sans Serif
Script

Colors
6b449b
886aae
eea4c8
f59195
fac994
3176b5
0555a3
cedeed
e4daeb

Requirements
Must have
• Targeted imagery, content and contact details
Nice to have
• personal profiles of people happy with our services

```html
<!DOCTYPE html>
<html lang="en">
<head>
<meta charset="utf-8">
<title>Calm Fern Healthcare – Brochure Spread</title>
<link href="https://fonts.googleapis.com/css2?family=Montserrat:wght@300;400;500;600;700&display=swap" rel="stylesheet">
<style>
  :root{
    --purple:#6b449b;
    --purple-deep:#55288f;
    --purple-soft:#886aae;
    --magenta:#c13a8f;
    --pink:#eea4c8;
    --lilac:#e4daeb;
    --ink:#3a3340;
    --body:#55505a;
    --paper:#f7f6f9;
    --backdrop:#4b4b4b;
  }
  *{box-sizing:border-box;margin:0;padding:0}
  html,body{width:1200px;height:789px;overflow:hidden}
  body{background:radial-gradient(circle at 55% 40%,#5a5a5a,var(--backdrop));font-family:"Montserrat",sans-serif;position:relative}
  .spread{position:absolute;left:100px;top:41px;width:1000px;height:707px;display:flex;box-shadow:0 18px 40px rgba(0,0,0,.45)}
  .page{position:relative;width:500px;height:707px;background:var(--paper);overflow:hidden}
  .page--left{border-bottom:3px solid var(--magenta)}
  .page--right{border-bottom:3px solid var(--purple)}
  .heading{font-weight:400;font-size:26px;line-height:1.2;color:var(--ink);letter-spacing:.2px}
  .heading em{font-style:normal;color:var(--magenta)}
  .abs{position:absolute}
  .heading-rule{height:1px;background:var(--magenta);opacity:.6}
  .copy{font-size:7.6px;line-height:1.5;color:var(--body);text-align:justify}
  .copy p+p{margin-top:9px}
  .photo{position:absolute;border-radius:50%;border:2px solid #fff;box-shadow:0 0 0 1px var(--purple-soft)}
  .photo--care{left:258px;top:120px;width:230px;height:230px;background:radial-gradient(circle at 45% 45%,#e8d7c2,#b99573 70%,#8c6a4e)}
  .photo--seniors{left:335px;top:345px;width:150px;height:150px;background:radial-gradient(circle at 50% 45%,#eae2e6,#b8b0bd 70%,#8c8591)}
  .photo--team{left:345px;top:560px;width:130px;height:130px;background:radial-gradient(circle at 50% 40%,#f2eef1,#c9bcc4 70%,#9b8b95)}
  .dot{position:absolute;border-radius:50%}
  .dot--purple{left:250px;top:95px;width:62px;height:62px;background:var(--purple-soft);opacity:.85}
  .dot--pink{left:440px;top:468px;width:44px;height:44px;background:var(--magenta);opacity:.75}
  .band{position:absolute;left:0;top:338px;width:330px;height:82px;background:linear-gradient(90deg,var(--purple-deep),var(--purple));color:#fff;padding:22px 0 0 58px}
  .band__light{display:block;font-weight:300;font-size:19px;letter-spacing:1.5px}
  .band__bold{display:block;font-weight:700;font-size:19px;letter-spacing:1.5px}
  .value{position:absolute;left:0;top:0;width:500px;height:395px;background:linear-gradient(135deg,var(--purple-deep),var(--purple) 60%,#7650a8)}
  .value .heading{position:absolute;color:#fff;left:90px;top:48px}
  .value__rule{position:absolute;left:90px;top:95px;width:360px;height:1px;background:rgba(255,255,255,.6)}
  .value__list{position:absolute;left:90px;top:112px;width:370px;list-style:none}
  .value__item{display:flex;align-items:center;gap:10px;height:36px;color:#fff;font-size:8px;line-height:1.35}
  .value__num{flex:none;width:20px;height:20px;border-radius:50%;border:1px solid rgba(255,255,255,.8);display:flex;align-items:center;justify-content:center;font-size:7.5px}
  .services-block{position:absolute;left:62px;top:410px;width:390px}
  .services-block .heading-rule{margin:6px 0 8px;width:390px}
  .services-intro{font-size:7.6px;color:var(--purple);margin:8px 0 6px}
  .services{list-style:none;font-size:9px;font-weight:600;color:var(--ink);line-height:1.35}
  .services li{display:flex;gap:6px;align-items:flex-start}
  .services svg{flex:none;margin-top:2px}
  .services small{display:block;font-size:8.5px;font-weight:600}
</style>
</head>
<body>
<main class="spread">
  <section class="page page--left">
    <h2 class="heading abs" style="left:40px;top:52px">Our <em>Philosophy</em></h2>
    <div class="heading-rule abs" style="left:40px;top:92px;width:230px"></div>
    <div class="dot dot--purple"></div>
    <div class="copy abs" style="left:40px;top:104px;width:205px">
      <p>Calm Fern Healthcare has a client focused approach which ensures it identifies individual client requirements to facilitate for a unique partnership without ambiguity. Our approach focuses on key pain areas of our clients which go beyond staffing needs. We ensure we look at the profile of the clients in your care to identify similar values and develop a "team based" system to ensure you always receive the same staff that meet your needs when you book your shifts.</p>
      <p>Our staff retention programs focus on the key drivers for staff to perform the work they do and whether their values are aligned to supporting vulnerable groups in society. With a proactive reward and recognition program, Calm Fern are well informed of areas of improvement to retain the very best talent. We believe our staff are a pillar to what we do, which is why we take every step to ensure they feel part of the great achievement and reward brought by supporting people who need assistance.</p>
    </div>
    <div class="photo photo--care" role="img" aria-label="Photo of a carer walking arm in arm with a smiling elderly woman"></div>
    <div class="band"><span class="band__light">REIMAGINING</span><span class="band__bold">HEALTHCARE</span></div>
    <div class="photo photo--seniors" role="img" aria-label="Photo of a group of happy seniors holding balloons"></div>
    <div class="dot dot--pink"></div>
    <h2 class="heading abs" style="left:40px;top:470px">Why Clients <em>Choose Us</em></h2>
    <div class="heading-rule abs" style="left:40px;top:510px;width:300px"></div>
    <div class="copy abs" style="left:40px;top:540px;width:400px">
      <p>Calm Fern Healthcare partners with likeminded organisations with a passion for making a difference to the lives of the vulnerable. We have differentiated ourselves by redefining the model of traditional staffing agencies and developed an obsessive desire to meet our clients needs. We genuinely care about what we do and know the impact under resourcing can do to day to day service delivery and overall quality outcomes.</p>
      <p>If you partner with us, we guarantee a tailored approach to meeting your needs.</p>
    </div>
  </section>

  <section class="page page--right">
    <div class="value">
      <h2 class="heading">Our Value Proposition</h2>
      <div class="value__rule"></div>
      <ol class="value__list">
        <li class="value__item"><span class="value__num">01</span>Our people are individually selected and participate in robust recruitment processes</li>
        <li class="value__item"><span class="value__num">02</span>We treat everyone with respect and believe our staff are the purpose of our existence</li>
        <li class="value__item"><span class="value__num">03</span>We are responsive to our clients priorities and walk along their journey to achieving operational excellence</li>
        <li class="value__item"><span class="value__num">04</span>We believe in ethical practices, transparency, and accountability</li>
        <li class="value__item"><span class="value__num">05</span>We are deliberate in our approach and have a passion for human services</li>
        <li class="value__item"><span class="value__num">06</span>We have a 'bias for action' and unceasingly pursue opportunities to change and adapt to the needs of our clients and environment</li>
      </ol>
    </div>
    <div class="services-block">
      <h2 class="heading">Our <em>Services</em></h2>
      <div class="heading-rule"></div>
      <div class="copy">
        <p>Our mission is to supply values driven, responsive, conscientious, and responsible personnel to the aged care sector, disability services, private and public health sectors. Our passion for human services and experience in recruitment, enables us to attract exceptional people with great values ready and willing to make a difference to the lives of vulnerable people.</p>
      </div>
      <p class="services-intro">We have a comprehensive database of the following personnel</p>
      <ul class="services">
        <li><svg width="9" height="9" viewBox="0 0 10 10"><circle cx="5" cy="5" r="4.4" fill="none" stroke="#c13a8f"/><path d="M3 5.2l1.4 1.4L7.2 3.8" fill="none" stroke="#c13a8f" stroke-width="1.1"/></svg><span>Registered Nurses<small>(Aged Care, Disability, Emergency, Public and Private healthcare)</small></span></li>
        <li><svg width="9" height="9" viewBox="0 0 10 10"><circle cx="5" cy="5" r="4.4" fill="none" stroke="#c13a8f"/><path d="M3 5.2l1.4 1.4L7.2 3.8" fill="none" stroke="#c13a8f" stroke-width="1.1"/></svg>Clinical Nurses</li>
        <li><svg width="9" height="9" viewBox="0 0 10 10"><circle cx="5" cy="5" r="4.4" fill="none" stroke="#c13a8f"/><path d="M3 5.2l1.4 1.4L7.2 3.8" fill="none" stroke="#c13a8f" stroke-width="1.1"/></svg>Nurse Practitioners</li>
        <li><svg width="9" height="9" viewBox="0 0 10 10"><circle cx="5" cy="5" r="4.4" fill="none" stroke="#c13a8f"/><path d="M3 5.2l1.4 1.4L7.2 3.8" fill="none" stroke="#c13a8f" stroke-width="1.1"/></svg>Enrolled Nurses</li>
        <li><svg width="9" height="9" viewBox="0 0 10 10"><circle cx="5" cy="5" r="4.4" fill="none" stroke="#c13a8f"/><path d="M3 5.2l1.4 1.4L7.2 3.8" fill="none" stroke="#c13a8f" stroke-width="1.1"/></svg>Assistants in Nursing (Carers/ PCA's)</li>
        <li><svg width="9" height="9" viewBox="0 0 10 10"><circle cx="5" cy="5" r="4.4" fill="none" stroke="#c13a8f"/><path d="M3 5.2l1.4 1.4L7.2 3.8" fill="none" stroke="#c13a8f" stroke-width="1.1"/></svg><span>Support Workers<small>(Disability, Community and Mental health)</small></span></li>
        <li><svg width="9" height="9" viewBox="0 0 10 10"><circle cx="5" cy="5" r="4.4" fill="none" stroke="#c13a8f"/><path d="M3 5.2l1.4 1.4L7.2 3.8" fill="none" stroke="#c13a8f" stroke-width="1.1"/></svg>Healthcare Endorsed Chefs and Cooks</li>
        <li><svg width="9" height="9" viewBox="0 0 10 10"><circle cx="5" cy="5" r="4.4" fill="none" stroke="#c13a8f"/><path d="M3 5.2l1.4 1.4L7.2 3.8" fill="none" stroke="#c13a8f" stroke-width="1.1"/></svg>Catering Assistants</li>
        <li><svg width="9" height="9" viewBox="0 0 10 10"><circle cx="5" cy="5" r="4.4" fill="none" stroke="#c13a8f"/><path d="M3 5.2l1.4 1.4L7.2 3.8" fill="none" stroke="#c13a8f" stroke-width="1.1"/></svg>Kitchen hands</li>
        <li><svg width="9" height="9" viewBox="0 0 10 10"><circle cx="5" cy="5" r="4.4" fill="none" stroke="#c13a8f"/><path d="M3 5.2l1.4 1.4L7.2 3.8" fill="none" stroke="#c13a8f" stroke-width="1.1"/></svg>Cleaners</li>
      </ul>
    </div>
    <div class="photo photo--team" role="img" aria-label="Photo of a smiling team of healthcare staff"></div>
  </section>
</main>
</body>
</html>
```